The Velvet Easel Co - Photos to Custom Oil Paintings

We need a website and logo designed and built allowing customers to purchase custom oil paintings. The paintings will come from a customers single photograph or even combination of photos. They will be able to complete a straight forward checkout process, selecting their desired medium (oil or charcoal painting), their desired size, the number of figures in the painting, the type of background required (as per photo or let the artist decide). Which will then automaticaly provide the customer with a price for the purchase. Allowing them to add a photo to the order which they can then submit with the order present in their personal account etc etc etc.
Theres one website in particular that i will be competing with. That is based in the US - http://www.brushmymoments.example
I wish to far exceed the appearence of the already present site.
At the moment i wish to include Quidlane in the payment process. Unless there are some cheaper, more cost efficient ways, please let me know.
The company name is The Velvet Easel Co. Domain has been purchased - www.thevelveteasel.example (via Nimbo Host - Linux)
I have no great sense of design, but the site must be straight forward, eye catching, engaging and give the customer a sense of high quality. Some kind of flash animation with pictures on the front page scrolling?
For myself, the admin side, ideally must be straight forward to maintain. The ability to update customers accounts with info (they will then be informed there is an update in their account etc)
The ability for automated emails from point of sale (sales orders with generated order numbers) to myself. Again automated emails to the customers once the "status" of their order or other information has been submitted to their account (by myself) or a similar system.
Updates
All,
Please note, the budget is able to increase subject to what additional work is needed. As far as the admin area goes. I am open to suggestions to ensure ease of use and efficiency.
Any questions, comments or ideas are fully welcomed.
Many thanks,
Martin Holloway
Industry/Entity Type
It Company
Logo Text
Logo styles of interest
Pictorial/Combination Logo
Abstract Logo
Wordmark Logo
Lettermark Logo
Look and feel
Each slider illustrates characteristics of the customer's brand and the style your logo design should communicate.

```html
<!DOCTYPE html>
<html lang="en">
<head>
<meta charset="utf-8">
<title>The Velvet Easel – Photos to Custom Oil Paintings</title>
<link href="https://fonts.googleapis.com/css2?family=Arimo:wght@400;700&display=swap" rel="stylesheet">
<style>
:root{
  --page:#ffffff;
  --ink:#222222;
  --muted:#555555;
  --navy:#2b4e9b;
  --navy-dark:#203d80;
  --red:#e0201f;
  --red-dark:#9c0c0c;
  --tick:#3aa635;
  --panel-top:#ffffff;
  --panel-bottom:#e9e9e9;
  --line:#cfcfcf;
  --black:#050505;
}
*{box-sizing:border-box;margin:0;padding:0}
html,body{width:1019px;height:1200px;overflow:hidden;background:var(--page)}
body{font-family:"Arimo",Arial,sans-serif;color:var(--ink);position:relative}
.abs{position:absolute}
.site{left:29px;top:28px;width:963px;height:1139px;border:1px solid #e3e3e3;border-radius:10px;box-shadow:0 0 6px rgba(0,0,0,.12);background:var(--page)}
.header{left:36px;top:34px;width:950px;height:112px;background:linear-gradient(#f2f2f2,#ffffff)}
.brand{left:47px;top:72px;font-size:31px;font-weight:700;color:var(--black);letter-spacing:2px;white-space:nowrap}
.login-title{left:709px;top:49px;font-size:14px;color:var(--navy)}
.field{top:74px;height:29px;border:1px solid #cfcfcf;border-radius:3px;background:#fff;font-size:11px;color:#555;padding:8px 8px}
.btn-login{left:926px;top:74px;width:58px;height:29px;background:var(--navy-dark);color:#fff;font-size:11px;text-align:center;line-height:29px;border-radius:3px}
.keep{left:711px;top:110px;font-size:11px;color:#444;display:flex;align-items:center;gap:8px}
.keep i{width:12px;height:12px;border:1px solid var(--navy);display:inline-block;background:#fff}
.forgot{left:862px;top:111px;font-size:11px;color:var(--red);text-decoration:underline}
.nav{left:30px;top:152px;width:961px;height:34px;background:var(--navy);display:flex;overflow:hidden}
.nav a{color:#fff;font-size:12px;text-decoration:none;line-height:34px;text-align:center;white-space:nowrap;flex:none}
.nav a.active{background:var(--red)}
.nav-item-1{width:125px}.nav-item-2{width:171px}.nav-item-3{width:103px}.nav-item-4{width:90px}
.nav-item-5{width:121px}.nav-item-6{width:55px}.nav-item-7{width:78px}.nav-item-8{width:107px}.nav-item-9{width:111px}
.panel{background:linear-gradient(var(--panel-top),var(--panel-bottom));border:1px solid #dcdcdc;border-radius:4px}
.features{left:37px;top:195px;width:247px;height:289px}
.features ul{list-style:none;position:absolute;left:8px;top:8px;width:225px}
.features li{height:38px;border-bottom:1px dashed #9a9a9a;display:flex;align-items:center;gap:12px;font-size:15px;color:#444;padding-left:6px}
.features li:last-child{border:none}
.hero{left:296px;top:195px;width:430px;height:289px;padding:6px;background:#fff}
.fill{width:100%;height:100%}
.hero .fill{background:linear-gradient(180deg,#0b0b0b 0%,#141414 40%,#c9a816 62%,#2a47a8 75%,#d4291c 92%)}
.testi{left:738px;top:195px;width:248px;height:289px;padding:8px 10px}
.testi h3{font-weight:400;font-size:17px;color:#444;border-bottom:1px dashed #9a9a9a;padding-bottom:4px;width:228px}
.testi .photo{float:left;width:98px;height:121px;margin:12px 8px 0 0;background:linear-gradient(#3b4f8c,#2a3564);border:1px solid #777}
.testi p{font-size:11.5px;line-height:21px;color:#444;text-align:justify;padding-top:10px}
.testi .more{position:absolute;right:6px;bottom:22px;font-size:12px;color:#444;text-decoration:underline}
.others{left:37px;top:505px;width:247px;height:395px;padding:12px 8px}
.others h3{font-weight:400;font-size:15px;line-height:20px;color:#555}
.others .grid{margin-top:9px;width:225px;height:159px;background:linear-gradient(135deg,#3a7a3a,#2a4fa0 45%,#c48a2a 75%,#7a3a2a)}
.others h4{font-weight:400;font-size:12.5px;color:#333;margin-top:17px}
.others p{font-size:12.5px;line-height:20px;color:#555;text-align:justify;margin-top:12px}
.bar{background:var(--black);color:#fff;font-size:15px;font-weight:700;border-radius:3px;height:32px;line-height:32px;padding-left:9px}
.welcome{left:295px;top:505px;width:432px}
.welcome p{font-size:11.5px;line-height:16px;color:#555;padding:7px 6px 0 6px;text-align:justify}
.welcome .more{display:block;text-align:right;padding-right:8px;margin-top:4px;font-size:12px;color:#444;text-decoration:underline}
.benefits{left:293px;top:622px;width:432px}
.benefits dl{padding:6px 6px 0 6px}
.benefits dt{display:inline;font-weight:700;font-size:12px;color:#333;letter-spacing:.3px}
.benefits dd{display:inline;font-size:11.5px;color:#555}
.benefits .item{margin-bottom:13px;line-height:14px}
.side{left:738px;top:505px;width:248px;height:395px}
.order-btn{position:absolute;left:17px;top:18px;width:218px;height:47px;border-radius:6px;background:linear-gradient(#d8332c,var(--red-dark));color:#fff;font-weight:700;font-size:13.5px;text-align:center;line-height:15px;padding-top:9px;box-shadow:0 2px 3px rgba(0,0,0,.3)}
.gift{position:absolute;left:48px;width:160px;height:78px;background:#fff;border:1px solid #ccc;box-shadow:0 1px 3px rgba(0,0,0,.2)}
.gift .ribbon{position:absolute;left:0;top:0;width:48px;height:76px;background:linear-gradient(90deg,#fff,#f2d0d0)}
.gift .band{position:absolute;left:0;top:30px;width:158px;height:5px;background:var(--red)}
.gift .l1{position:absolute;left:49px;top:8px;font-size:14px;line-height:16px;color:#333;white-space:nowrap}
.gift .l2{position:absolute;left:56px;top:40px;font-size:14px;line-height:16px;color:var(--red);white-space:nowrap}
.gift .l3{position:absolute;left:62px;top:58px;font-size:9.5px;color:#333;white-space:nowrap}
.chat{position:absolute;left:47px;top:183px;width:161px;height:77px;background:#fff}
.chat b{position:absolute;left:15px;top:22px;font-size:16px;line-height:18px;color:#b0131b}
.chat .agent{position:absolute;left:82px;top:0;width:79px;height:77px;background:linear-gradient(#f4e2cf,#e9c9a5)}
.strip{left:37px;top:918px;width:949px;height:164px;border-top:3px solid #e6e6e6;background:linear-gradient(#ffffff,#eeeeee)}
.pets{position:absolute;left:14px;top:10px;display:flex;gap:8px}
.pet{width:125px;text-align:center;font-size:12.5px;color:#555}
.pet .fill{height:125px;border:1px solid #ccc;background:radial-gradient(circle at 50% 45%,#c88a3a 0,#7a8a2a 40%,#4a6a1a 70%,#f5e4d2 90%)}
.pet span{display:block;margin-top:6px}
.pay{left:37px;top:1092px;display:flex;gap:3px;align-items:center}
.pay i{width:31px;height:21px;display:block;border-radius:2px;background:#6a7ea8;border:1px solid #9aa}
.pay b{margin-left:8px;font-size:21px;color:var(--navy-dark);font-weight:700}
.social{left:916px;top:1087px;display:flex;gap:8px}
.social i{width:30px;height:30px;border-radius:4px;display:block}
.social i:first-child{background:#3b5a9a}
.social i:last-child{background:#4fb8e6}
.footer-line{left:30px;top:1122px;width:961px;border-top:1px solid #ddd}
.links{left:30px;width:961px;text-align:center;font-size:12px;color:#444;word-spacing:1px;white-space:nowrap}
.links span{padding:0 8px;color:#777}
</style>
</head>
<body>
<div class="abs site"></div>

<header>
  <div class="abs header"></div>
  <div class="abs brand">THE VELVET EASEL</div>
  <div class="abs login-title">Member Login :</div>
  <div class="abs field" style="left:708px;width:97px">Username</div>
  <div class="abs field" style="left:818px;width:97px;font-size:14px;padding-top:4px;letter-spacing:1px">••••••••••</div>
  <div class="abs btn-login">Login</div>
  <div class="abs keep"><i></i>Keep me logged in</div>
  <div class="abs forgot">Forgot Your Password ?</div>
</header>

<nav class="abs nav">
  <a class="nav-item-1">HOW IT WORKS</a><a class="nav-item-2">ORDER YOUR PAINTING</a><a class="nav-item-3 active">GALLERIES</a><a class="nav-item-4">GIFT IDEAS</a><a class="nav-item-5">TESTIMONIALS</a><a class="nav-item-6">FAQ</a><a class="nav-item-7">PRICES</a><a class="nav-item-8">GUARANTEE</a><a class="nav-item-9">CONTACT US</a>
</nav>

<section class="abs panel features">
  <ul>
    <li><svg width="16" height="16" viewBox="0 0 16 16"><path d="M1 9l4 5L15 1" fill="none" stroke="#3aa635" stroke-width="2.5"/></svg>Real Live Painters</li>
    <li><svg width="16" height="16" viewBox="0 0 16 16"><path d="M1 9l4 5L15 1" fill="none" stroke="#3aa635" stroke-width="2.5"/></svg>Affordable Prices</li>
    <li><svg width="16" height="16" viewBox="0 0 16 16"><path d="M1 9l4 5L15 1" fill="none" stroke="#3aa635" stroke-width="2.5"/></svg>Quick Turnaround</li>
    <li><svg width="16" height="16" viewBox="0 0 16 16"><path d="M1 9l4 5L15 1" fill="none" stroke="#3aa635" stroke-width="2.5"/></svg>Free Photo Editing</li>
    <li><svg width="16" height="16" viewBox="0 0 16 16"><path d="M1 9l4 5L15 1" fill="none" stroke="#3aa635" stroke-width="2.5"/></svg>Real Live Painters</li>
    <li><svg width="16" height="16" viewBox="0 0 16 16"><path d="M1 9l4 5L15 1" fill="none" stroke="#3aa635" stroke-width="2.5"/></svg>Affordable Prices</li>
    <li><svg width="16" height="16" viewBox="0 0 16 16"><path d="M1 9l4 5L15 1" fill="none" stroke="#3aa635" stroke-width="2.5"/></svg>Quick Turnaround</li>
  </ul>
</section>

<section class="abs panel hero">
  <div class="fill" role="img" aria-label="Featured abstract painting in black, yellow, blue and red"></div>
</section>

<section class="abs panel testi">
  <h3>Testimonials</h3>
  <div class="photo" role="img" aria-label="Customer portrait photo"></div>
  <p>"This painting is a Christmas gift for my mom. My brother is currently serving in Afghanistan and I wanted her to have a special gift this year. I`m so happy with this painting, you captured every detail. Thank you!"</p>
  <span class="more">Read more</span>
</section>

<section class="abs panel others">
  <h3>Other great products of The Velvet Easel studios:</h3>
  <div class="grid" role="img" aria-label="Collage of canvas print samples"></div>
  <h4>Other great products of The Velvet Easel:</h4>
  <p>Print your photo on canvas simply as is, or give it a new look by choosing one of our amazing styles Canvas Prints</p>
</section>

<section class="abs welcome">
  <div class="bar">Welcome to The Velvet Easel</div>
  <p>The VelvetEasel.example is the world leader in Photo to Painting services. Our portrait painters will create a 100% Handmade work of art as a perfect gift for your loved ones.</p>
  <span class="more">Read more</span>
</section>

<section class="abs benefits">
  <div class="bar">Let Us Paint Your Life!</div>
  <dl>
    <div class="item"><dt>Quality</dt> <dd>- All our artworks are created by hand by experienced professional portrait artists using top quality paints and materials.</dd></div>
    <div class="item"><dt>Prices</dt> <dd>- We ask for only 20% advance payment. Our prices are affordable - oil portraits on canvas from $99 and charcoal portraits from $69 only!</dd></div>
    <div class="item"><dt>Design</dt> <dd>- Our portrait painters can combine several photos into 1 portrait painting.</dd></div>
    <div class="item"><dt>Handpainted</dt> <dd>- Our artworks are hand painted by real painting artists. They are NOT computer generated.</dd></div>
    <div class="item"><dt>Delivery</dt> <dd>- Our unique express service makes our portraits a great gift idea for anniversary gifts, birthday gifts, photo gifts or any unique gifts.</dd></div>
    <div class="item"><dt>Variety</dt> <dd>- Our artists can handle creation of beautiful pet portraits, family portraits, self portraits and much more. Visit our Galleries section for more!</dd></div>
  </dl>
</section>

<aside class="abs panel side">
  <div class="order-btn">Order your painting now<br>in 3 easy steps</div>
  <div class="gift" style="top:86px">
    <div class="band"></div><div class="ribbon" role="img" aria-label="Red gift ribbon"></div>
    <span class="l1">Get our special</span><span class="l2">Gift certificate</span><span class="l3">for your loved ones</span>
  </div>
  <div class="chat">
    <b>Live<br>Chat</b>
    <div class="agent" role="img" aria-label="Support agent with headset"></div>
  </div>
  <div class="gift" style="top:288px">
    <div class="band"></div><div class="ribbon" role="img" aria-label="Red gift ribbon"></div>
    <span class="l1">Get our special</span><span class="l2">Gift certificate</span><span class="l3">for your loved ones</span>
  </div>
</aside>

<section class="abs strip">
  <div class="pets">
    <div class="pet"><div class="fill" role="img" aria-label="Painted puppy held in hands"></div><span>Pet portraits</span></div>
    <div class="pet"><div class="fill" role="img" aria-label="Painted puppy held in hands"></div><span>Pet portraits</span></div>
    <div class="pet"><div class="fill" role="img" aria-label="Painted puppy held in hands"></div><span>Pet portraits</span></div>
    <div class="pet"><div class="fill" role="img" aria-label="Painted puppy held in hands"></div><span>Pet portraits</span></div>
    <div class="pet"><div class="fill" role="img" aria-label="Painted puppy held in hands"></div><span>Pet portraits</span></div>
    <div class="pet"><div class="fill" role="img" aria-label="Painted puppy held in hands"></div><span>Pet portraits</span></div>
    <div class="pet"><div class="fill" role="img" aria-label="Painted puppy held in hands"></div><span>Pet portraits</span></div>
  </div>
</section>

<footer>
  <div class="abs pay"><i></i><i></i><i></i><i></i><b>Quidlane</b></div>
  <div class="abs social"><i></i><i></i></div>
  <div class="abs footer-line"></div>
  <div class="abs links" style="top:1127px">Portrait painting<span>|</span>About us<span>|</span>Partners<span>|</span>Affiliates<span>|</span>Photo tips<span>|</span>Terms and conditions<span>|</span>Articles<span>|</span>Products<span>|</span>Sitemap</div>
  <div class="abs links" style="top:1147px">Other Languages: Portrait painting<span>|</span>Photo sur toile<span>|</span>Portraitmalerei<span>|</span>Transformar fotos<span>|</span>Foto su tela<span>|</span>Schilderijen</div>
</footer>
</body>
</html>
```